Label Design for RTD Cocktail Line Tovelin Spirits

Tovelin Spirits is a line of Indian-inspired artisan cocktails that "brings the bartender home" for professional men and women who like the finer things in life but don’t always have the time to treat themselves. No need for a multitude of expensive and hard-to-find ingredients, time consuming recipes, or a mixologist.

Our line of 3 open and serve cocktails blends a range of premium spirits with exotic ingredients so you can conveniently raise a glass for any of life’s celebrations.

Our bottle is the 750ml Claret bottle with Quarnet (screw cap) closure and will be covered entirely in a shrink sleeve (so potentially anything can be designed for any part of the bottle). We want the bottle to pop on the shelf so it should look different than what’s already out there (Velvet Moth, Galdrova, Merlusa ready to drink cocktails). We are looking for a sexy design that's polished/sleek.
Updates

Project Deadline Extended
Reason: Hello designers! Tovelin Spirits is so impressed with what we have received thus far and we would like to give some of the designers a few extra days to make the edits we requested. It's never too late to submit! Thank you all!

Industry/Entity Type

It Professional

Requirements
Must have
• Front of bottle
* “Tovelin Spirits” name and Peacock Logo- but feel free to pull the elements apart and use them on the bottle in different ways
* Open & Serve
* 12% ALC/VOL
* 750 ml
* 3 different labels in a theme for
-Borvelle
-Faluntera
-Pomadrine

Borvelle Ideas- soft brown palate, the ingredients in chai spice (cloves, cardamom pods, nutmeg, black peppercorns, star anise, and cinnamon stick)

Faluntera Ideas -cool and refreshing, pale green shade (not clashing with logo), graphics of fresh mint leaves, green chili, lime, cucumber

Pomadrine Ideas- soft/pale pink shades, graphics of lychi fruit (outer red shell and inner pink flesh), ginger

Back of bottle
* explanation of the 3 cocktails
Borvelle: Forget what you think you know about chai, this is not the Queen’s tea-time drink! Borvelle is a smooth, sweetly -spiced cocktail made with vodka, black tea, and a combination of aromatic spices. This velvety cocktail is rich without being heavy. Enjoy chilled or over ice anytime.

Faluntera: Faluntera can’t make up its mind! This fusion of zesty lime, sweet mint, earthy cucumber and spicy chilies is so refreshing you’ll crave it on a hot summer day or a cool winter’s night. The exotic botanicals in gin add a complexity to the cocktail making this a refreshing but potent drink! Enjoy chilled or over ice anytime.

Pomadrine: East meet West. Delicate lychi meet hard-hitting whiskey. Pomadrine will tempt you senses with flavor, fragrance and beauty. The peppery kick of ginger and the intensity of the un-aged whiskey are softened by lychi’s intoxicating scent and subtle, sweet finish.

Please include
1. Bottled By QRW Spirits Company
2. Sample barcode (where you would place it in your design)
3. www.TovelinSpirits.example
4. GOVERNMENT WARNING: (1) According to the Surgeon General, women should not drink alcoholic beverages during pregnancy because of the risk of birth defects. (2) Consumption of alcoholic beverages impairs your ability to drive a car or operate machinery, and may cause health problems.

Optional to include
*"Bring the Bartender Home"
*"Tovelin Spirits” name and Peacock Logo on the back
*Entirely black sleeve with contrasting design

FYI the Fonts used in our logo are Geosans Light and Prakrta, but feel free to use other complimentary fonts on the other aspects.
Nice to have
• Optional to include

```html
<!DOCTYPE html>
<html lang="en">
<head>
<meta charset="utf-8">
<title>Tovelin Spirits – Cocktail Labels</title>
<link rel="stylesheet" href="https://fonts.googleapis.com/css2?family=Josefin+Sans:wght@300&display=swap">
<style>
  :root {
    --canvas: #ffffff;
    --sleeve-top: #e9e9ea;
    --sleeve-mid: #f7f7f7;
    --sleeve-edge: #d8d8da;
    --ink: #1c1c1c;
    --brand: #1f8fae;
    --faluntera: #89c540;
    --borvelle: #dbaf8c;
    --pomadrine: #f2a3a0;
    --ribbon-dark: #0e4f8e;
    --ribbon-light: #9fd3f0;
    --on-colour: #ffffff;
  }
  * { box-sizing: border-box; margin: 0; padding: 0; }
  html, body { width: 1142px; height: 1200px; overflow: hidden; background: var(--canvas); }
  body { position: relative; font-family: "Josefin Sans", "Futura", sans-serif; font-weight: 300; }

  .label {
    position: absolute;
    width: 308px;
    height: 1062px;
    overflow: hidden;
    background: linear-gradient(90deg, var(--sleeve-edge) 0%, var(--sleeve-mid) 22%, var(--sleeve-top) 60%, var(--sleeve-edge) 100%);
    box-shadow: 3px 4px 6px rgba(0,0,0,0.35);
  }
  .label--faluntera { left: 63px; top: 66px; --flavour: var(--faluntera); }
  .label--borvelle  { left: 416px; top: 68px; --flavour: var(--borvelle); }
  .label--pomadrine { left: 765px; top: 70px; --flavour: var(--pomadrine); }

  .brand {
    position: absolute;
    top: 112px;
    left: 0; right: 0;
    text-align: center;
    color: var(--brand);
    line-height: 1;
  }
  .brand__name { display: block; font-size: 30px; letter-spacing: 1px; }
  .brand__sub { display: block; font-size: 10px; letter-spacing: 5px; margin-top: 4px; }

  .product-name {
    position: absolute;
    left: 96px;
    top: 190px;
    width: 110px;
    height: 570px;
  }
  .product-name text {
    font-family: "Josefin Sans", "Futura", sans-serif;
    font-weight: 300;
    font-size: 116px;
    fill: var(--ink);
  }

  .serve {
    position: absolute;
    top: 790px;
    left: 0; right: 0;
    text-align: center;
    font-size: 27px;
    color: var(--ink);
    letter-spacing: 0.5px;
  }

  .base {
    position: absolute;
    left: 0;
    top: 840px;
    width: 308px;
    height: 222px;
  }
  .base__fill { fill: var(--flavour); }

  .specs {
    position: absolute;
    top: 975px;
    left: 0; right: 0;
    text-align: center;
    color: var(--on-colour);
    font-size: 22px;
    line-height: 27px;
  }
</style>
</head>
<body>
  <svg width="0" height="0" style="position:absolute">
    <defs>
      <linearGradient id="ribbon" x1="0" x2="1" y1="0" y2="0">
        <stop offset="0" stop-color="var(--ribbon-dark)"/>
        <stop offset="0.45" stop-color="var(--ribbon-light)"/>
        <stop offset="1" stop-color="var(--ribbon-dark)"/>
      </linearGradient>
    </defs>
  </svg>

  <section class="label label--faluntera">
    <div class="brand"><span class="brand__name">Tovelin</span><span class="brand__sub">SPIRITS</span></div>
    <svg class="product-name" viewBox="0 0 110 570">
      <text transform="translate(100 565) rotate(-90)" textLength="555" lengthAdjust="spacingAndGlyphs">FALUNTERA</text>
    </svg>
    <p class="serve">OPEN &amp; SERVE</p>
    <svg class="base" viewBox="0 0 308 222">
      <path class="base__fill" d="M0,22 C60,0 150,8 308,58 L308,222 L0,222 Z"/>
      <path d="M0,22 C60,0 150,8 308,58" fill="none" stroke="url(#ribbon)" stroke-width="7"/>
    </svg>
    <p class="specs">12% ALC/VOL<br>750 ml</p>
  </section>

  <section class="label label--borvelle">
    <div class="brand"><span class="brand__name">Tovelin</span><span class="brand__sub">SPIRITS</span></div>
    <svg class="product-name" viewBox="0 0 110 570">
      <text transform="translate(100 565) rotate(-90)" textLength="555" lengthAdjust="spacingAndGlyphs">BORVELLE</text>
    </svg>
    <p class="serve">OPEN &amp; SERVE</p>
    <svg class="base" viewBox="0 0 308 222">
      <path class="base__fill" d="M0,22 C60,0 150,8 308,58 L308,222 L0,222 Z"/>
      <path d="M0,22 C60,0 150,8 308,58" fill="none" stroke="url(#ribbon)" stroke-width="7"/>
    </svg>
    <p class="specs">12% ALC/VOL<br>750 ml</p>
  </section>

  <section class="label label--pomadrine">
    <div class="brand"><span class="brand__name">Tovelin</span><span class="brand__sub">SPIRITS</span></div>
    <svg class="product-name" viewBox="0 0 110 570">
      <text transform="translate(100 565) rotate(-90)" textLength="555" lengthAdjust="spacingAndGlyphs">POMADRINE</text>
    </svg>
    <p class="serve">OPEN &amp; SERVE</p>
    <svg class="base" viewBox="0 0 308 222">
      <path class="base__fill" d="M0,22 C60,0 150,8 308,58 L308,222 L0,222 Z"/>
      <path d="M0,22 C60,0 150,8 308,58" fill="none" stroke="url(#ribbon)" stroke-width="7"/>
    </svg>
    <p class="specs">12% ALC/VOL<br>750 ml</p>
  </section>
</body>
</html>
```